beauty salon

providing waxing services from a home base this must include which I will provide a price list and an address

Industry/Entity Type

Beauty Salon

Font styles to use
Script

Colors

Designer to choose colors to be used in the design.

```html
<!DOCTYPE html>
<html lang="en">
<head>
<meta charset="utf-8">
<title>Beauty Therapist – Sienna's Garden Salon</title>
<link href="https://fonts.googleapis.com/css2?family=Arimo:wght@400;700&family=Josefin+Sans:wght@300;400;600&display=swap" rel="stylesheet">
<style>
  :root{
    --sky-light:#d9f1fb;
    --sky:#a9dcf2;
    --sky-deep:#7cc6e8;
    --plum:#8b3c8f;
    --plum-deep:#7a2f80;
    --ink:#111111;
    --white:#ffffff;
    --teal:#3a8f8a;
    --skin:#e6b08c;
    --skin-light:#f2cfb2;
  }
  *{margin:0;padding:0;box-sizing:border-box}
  html,body{width:1200px;height:850px;overflow:hidden}
  body{font-family:"Arimo",Arial,sans-serif;color:var(--ink)}
  .flyer{
    position:relative;width:1200px;height:850px;overflow:hidden;
    background:linear-gradient(135deg,var(--sky-light) 0%,var(--sky) 45%,var(--sky-deep) 100%);
  }
  .model-photo{
    position:absolute;left:0;top:0;width:420px;height:768px;
    background:linear-gradient(90deg,var(--skin) 0%,var(--skin-light) 55%,rgba(242,207,178,0) 100%);
  }
  .title{
    position:absolute;left:366px;top:34px;width:820px;
    font-family:"Josefin Sans",sans-serif;font-weight:400;
    font-size:66px;letter-spacing:6px;color:var(--white);text-align:center;line-height:1;
    white-space:nowrap;
  }
  .subtitle{
    position:absolute;left:366px;top:103px;width:820px;text-align:center;
    font-family:"Josefin Sans",sans-serif;font-weight:400;
    font-size:23px;letter-spacing:1.5px;color:var(--white);white-space:nowrap;
  }
  .section-heading{
    position:absolute;left:440px;
    font-family:"Josefin Sans",sans-serif;font-weight:400;
    font-size:34px;letter-spacing:2px;color:var(--plum);line-height:1;white-space:nowrap;
  }
  .price-list{position:absolute;list-style:none;font-weight:700;font-size:20px;line-height:30px;white-space:nowrap}
  .price-list li{display:flex}
  .price-list .item{display:inline-block;white-space:nowrap;flex-shrink:0}
  .ladies-a .item{width:140px}
  .ladies-b .item{width:171px}
  .eye-a .item{width:143px}
  .eye-b .item{width:171px}
  .men-a .item{width:185px}
  .men-b .item{width:168px}
  .offer-badge{
    position:absolute;left:935px;top:203px;width:186px;height:186px;border-radius:50%;
    background:var(--plum);color:var(--white);text-align:center;font-weight:700;
    display:flex;flex-direction:column;justify-content:center;align-items:center;
  }
  .offer-badge .percent{font-size:72px;line-height:.95;letter-spacing:-2px}
  .offer-badge .terms{font-size:20px;line-height:23px;margin-top:4px}
  .opening-hours{
    position:absolute;left:903px;top:432px;width:280px;text-align:center;
    font-weight:700;font-size:20px;line-height:29px;white-space:nowrap;
  }
  .opening-hours .label{color:var(--ink)}
  .opening-hours .slot{color:var(--plum)}
  .salon-name{
    position:absolute;left:840px;top:723px;width:350px;text-align:center;
    font-family:"Josefin Sans",sans-serif;font-weight:400;font-size:30px;color:var(--teal);
    display:flex;align-items:center;justify-content:center;gap:10px;white-space:nowrap;
  }
  .salon-name .dot{width:12px;height:12px;border-radius:50%;background:var(--teal)}
  .contact-bar{
    position:absolute;left:0;top:768px;width:1200px;height:82px;background:var(--plum-deep);
    color:var(--white);display:flex;align-items:center;justify-content:space-between;padding:0 22px 0 44px;
    white-space:nowrap;
  }
  .contact-bar .mobile{font-weight:700;font-size:35px}
  .contact-bar .address{font-family:"Josefin Sans",sans-serif;font-weight:400;font-size:31px;letter-spacing:1.5px}
</style>
</head>
<body>
<main class="flyer">
  <div class="model-photo" role="img" aria-label="Photo of a woman in a purple bikini wearing beaded necklaces and bracelets"></div>

  <h1 class="title">BEAUTY THERAPIST</h1>
  <p class="subtitle">SIENNA DIPLOMA OF BEAUTY THERAPY AT MARLOW ACADEMY</p>

  <h2 class="section-heading" style="top:180px">LADY'S WAXING</h2>
  <ul class="price-list ladies-a" style="left:442px;top:217px">
    <li><span class="item">Eyebrow</span>$8</li>
    <li><span class="item">Upper lip</span>$8</li>
    <li><span class="item">Chin</span>$8</li>
    <li><span class="item">Face wax</span>$25</li>
    <li><span class="item">Bikini line</span>$15</li>
    <li><span class="item">G string</span>$20</li>
    <li><span class="item">½ Brazilian</span>$30</li>
  </ul>
  <ul class="price-list ladies-b" style="left:687px;top:217px">
    <li><span class="item">Full Brazilian</span>$40</li>
    <li><span class="item">Half arm</span>$20</li>
    <li><span class="item">Upper half arm</span>$20</li>
    <li><span class="item">Full arm</span>$25</li>
    <li><span class="item">Half leg</span>$15</li>
    <li><span class="item">Upper leg</span>$20</li>
    <li><span class="item">¾ Leg</span>$25</li>
    <li><span class="item">Full leg</span>$35</li>
  </ul>

  <h2 class="section-heading" style="top:468px">EYE ENHANCEMENT</h2>
  <ul class="price-list eye-a" style="left:442px;top:499px">
    <li><span class="item">Eyebrow Tint</span>$12</li>
  </ul>
  <ul class="price-list eye-b" style="left:687px;top:499px">
    <li><span class="item">Eyelash Tint</span>$15</li>
  </ul>

  <h2 class="section-heading" style="top:551px">MEN'S WAXING</h2>
  <ul class="price-list men-a" style="left:442px;top:585px">
    <li><span class="item">Eyebrow</span>$10</li>
    <li><span class="item">Half arm</span>$20</li>
    <li><span class="item">Upper half arm</span>$25</li>
    <li><span class="item">Full arm</span>$30</li>
    <li><span class="item">Half leg</span>$25</li>
  </ul>
  <ul class="price-list men-b" style="left:690px;top:585px">
    <li><span class="item">Full leg</span>$45</li>
    <li><span class="item">Chest wax</span>$40</li>
    <li><span class="item">Back wax</span>$35</li>
  </ul>

  <div class="offer-badge">
    <span class="percent">10%</span>
    <span class="terms">Discount on<br>first treatment.</span>
  </div>

  <div class="opening-hours">
    <div class="label">NOW OPEN:</div>
    <div class="slot">Wednesday</div>
    <div class="slot">10am - 4pm</div>
    <div class="slot">Fridays</div>
    <div class="slot">10am - 7pm</div>
    <div class="slot">Saturday 10am - 4pm</div>
  </div>

  <div class="salon-name"><span class="dot"></span>Sienna's Garden Salon</div>

  <footer class="contact-bar">
    <span class="mobile">Mobile: 0400 555 123</span>
    <span class="address">12 FINCH LANE - KESTREL PARK</span>
  </footer>
</main>
</body>
</html>
```